Palomyn - Managed Service Provider Brochure

Our company has launched a new division, a "Managed Service Provider (MSP)" division and we are looking for a new bifold brochure to market our company.
This new service provides our clients a vendor management solution to save money and control their procurement process. We would like to maintain the same color scheme of black and red as the core colors along our logo.
We have provided a recent powerpoint presentation done by our team containing the copy material that can be used for this project. We do not require the images stay the same so feel free to incorporate what works best in the design.
Thank you.
It Company

```html
<!DOCTYPE html>
<html lang="en">
<head>
<meta charset="utf-8">
<title>Palomyn – MSP Brochure</title>
<link href="https://fonts.googleapis.com/css2?family=Arimo:ital,wght@0,400;0,700;1,400&display=swap" rel="stylesheet">
<style>
  :root {
    --stage: #2a2a2c;
    --red: #e31b23;
    --red-deep: #c8161d;
    --panel-gray: #e6e7e8;
    --ink: #1d1d1f;
    --muted: #8a8b8d;
    --white: #ffffff;
    --stripe-gray: #c9cacc;
  }
  * { margin: 0; padding: 0; box-sizing: border-box; }
  html, body { width: 907px; height: 1200px; overflow: hidden; }
  body { background: var(--stage); font-family: "Arimo", Arial, sans-serif; position: relative; }

  .spread { position: absolute; left: 90px; width: 743px; overflow: hidden; box-shadow: 0 6px 14px rgba(0,0,0,.5); }
  .spread--outer { top: 50px; height: 527px; background: var(--panel-gray); }
  .spread--inner { top: 620px; height: 525px; background: var(--white); }
  .shapes { position: absolute; inset: 0; }
  .abs { position: absolute; }

  .brand { font-size: 36px; color: var(--ink); letter-spacing: -0.5px; line-height: 1; }
  .brand--light { color: var(--muted); font-size: 30px; }

  .contact { color: var(--ink); }
  .contact--outer { font-style: italic; font-size: 12.5px; line-height: 16px; }
  .contact--inner { font-size: 10px; line-height: 13px; }

  .cover-title { color: var(--white); font-size: 23px; line-height: 30px; }
  .cover-title em { font-style: italic; font-weight: 400; }
  .cover-title strong { color: var(--ink); font-weight: 700; }
  .cover-lede { color: var(--white); font-size: 11px; line-height: 14px; width: 262px; }

  .intro { font-size: 10.5px; line-height: 13.5px; color: #333; width: 288px; }

  .inner-title { font-size: 22px; line-height: 30px; font-weight: 700; color: var(--white); text-shadow: 0 1px 3px rgba(0,0,0,.45); }
  .inner-title em { color: var(--red); font-weight: 400; }
</style>
</head>
<body>

<section class="spread spread--outer">
  <svg class="shapes" width="743" height="527" viewBox="0 0 743 527">
    <defs>
      <linearGradient id="office-tones" x1="0" y1="0" x2="0" y2="1">
        <stop offset="0" stop-color="#eef1f4"/>
        <stop offset="0.6" stop-color="#d8dde2"/>
        <stop offset="1" stop-color="#9a9ea3"/>
      </linearGradient>
    </defs>
    <rect x="220" y="0" width="523" height="527" fill="url(#office-tones)" role="img" aria-label="Photo: business people meeting in a bright office atrium"/>
    <polygon points="228,0 743,0 743,272 630,318" fill="var(--red-deep)"/>
    <polygon points="228,0 238,0 630,305 630,318" fill="#55575a"/>
    <polygon points="220,315 305,272 743,500 743,527 690,527" fill="var(--white)"/>
    <polygon points="220,318 300,282 690,527 220,527" fill="var(--red)"/>
  </svg>

  <div class="abs" style="left:414px; top:36px;">
    <h1 class="cover-title"><em>Management Service</em><br><strong>Program Vms Technology</strong></h1>
  </div>
  <p class="abs cover-lede" style="left:452px; top:108px;">Palomyn National Staffing works to unite the best talent with the best employment across a national and geographical scope.</p>

  <div class="abs brand" style="left:16px; top:384px;">palomyn</div>
  <p class="abs contact contact--outer" style="left:16px; top:442px;">Phone: (555) 210-4400<br>Email: hello@palomynstaff.com</p>

  <div class="abs brand" style="left:390px; top:458px; font-size:32px;">palomyn</div>
</section>

<section class="spread spread--inner">
  <svg class="shapes" width="743" height="525" viewBox="0 0 743 525">
    <defs>
      <linearGradient id="team-tones" x1="0" y1="0" x2="1" y2="1">
        <stop offset="0" stop-color="#d9dadc"/>
        <stop offset="0.5" stop-color="#8c8e92"/>
        <stop offset="1" stop-color="#3b3c40"/>
      </linearGradient>
    </defs>
    <rect x="0" y="0" width="370" height="398" fill="var(--panel-gray)"/>
    <rect x="0" y="404" width="370" height="3" fill="var(--red)"/>
    <rect x="370" y="0" width="373" height="525" fill="url(#team-tones)" role="img" aria-label="Photo: a group of business professionals standing together"/>
    <polygon points="743,180 743,525 455,525" fill="var(--white)"/>
    <polygon points="743,128 743,185 525,465 500,445" fill="var(--red)"/>
    <polygon points="500,445 525,465 520,470 496,452" fill="#8e1015"/>
    <polygon points="743,210 743,228 650,352 636,342" fill="var(--stripe-gray)"/>
    <polygon points="640,380 655,392 560,525 540,525" fill="var(--stripe-gray)"/>
  </svg>

  <p class="abs intro" style="left:35px; top:112px;">At Palomyn National Staffing we have found that success can be measured by the strength of the relationships that we cultivate with both our candidates and clients. We have extended this principle toward the relationships that we sustain with MSP and VMS providers as well.</p>

  <h2 class="abs inner-title" style="left:386px; top:222px;">Management<br>Service <em>Program</em><br><em>Vms</em> Technology</h2>

  <div class="abs brand brand--light" style="left:192px; top:425px;">palomyn</div>
  <p class="abs contact contact--inner" style="left:192px; top:472px;">Phone: (555) 210-4400<br>Email: hello@palomynstaff.com</p>

  <div class="abs brand" style="left:596px; top:460px; font-size:30px;">palomyn</div>
</section>

</body>
</html>
```